Australian Software Consultancy needs new Business Card Design

Design Business Card based on existing design artefacts (attached). We are open to all designs. As its a 2 sided design and we thought it might be quite striking to have one side with a black background and te other side with a white background.

Target Market(s)

Financial Services mainly.

Industry/Entity Type

Business

Contact Information for Business Card

Name :
Position :
Email :

Requirements
Must have
• Funky design using our existing assets

```html
<!DOCTYPE html>
<html lang="en">
<head>
<meta charset="utf-8">
<title>Keen Field – Business Card</title>
<link href="https://fonts.googleapis.com/css2?family=Quicksand:wght@500;700&display=swap" rel="stylesheet">
<style>
  :root {
    --canvas: #d9d9d9;
    --card-dark: #333133;
    --glow-tone: #4a494b;
    --card-light: #ffffff;
    --ink: #231f20;
    --accent: #e31b23;
    --white: #ffffff;
  }
  * { margin: 0; padding: 0; box-sizing: border-box; }
  html, body { width: 1200px; height: 1200px; overflow: hidden; }
  body {
    background: var(--canvas);
    position: relative;
    font-family: "Quicksand", sans-serif;
  }
  .card {
    position: absolute;
    left: 182px;
    width: 834px;
    height: 463px;
    overflow: hidden;
    box-shadow: 0 4px 14px rgba(0,0,0,0.25);
  }
  .card--front { top: 82px; background: var(--card-dark); }
  .card--back { top: 669px; background: var(--card-light); }

  .illustration-area {
    position: absolute;
    inset: 0;
    background: radial-gradient(ellipse 480px 360px at 72% 30%, var(--glow-tone) 0%, var(--glow-tone) 35%, var(--card-dark) 100%);
  }

  .front-wordmark {
    position: absolute;
    left: 190px;
    top: 200px;
    font-weight: 700;
    font-size: 70px;
    letter-spacing: 4px;
    color: var(--white);
    line-height: 1;
    white-space: nowrap;
  }

  .back-wordmark {
    position: absolute;
    left: 30px;
    top: 24px;
    font-weight: 700;
    font-size: 31px;
    color: var(--ink);
    line-height: 1;
    white-space: nowrap;
  }

  .contact {
    position: absolute;
    display: flex;
    align-items: flex-start;
    gap: 12px;
    color: var(--ink);
    font-weight: 500;
    font-size: 22px;
    line-height: 27px;
    white-space: nowrap;
  }
  .contact svg { flex: none; width: 34px; height: 34px; }
  .contact--person { left: 555px; top: 20px; }
  .contact--person .contact-text { padding-top: 9px; }
  .contact--email { left: 527px; top: 411px; }
  .contact--email .contact-text { padding-top: 10px; }

  .brand-lockup {
    position: absolute;
    left: 0; right: 0;
    top: 183px;
    display: flex;
    align-items: center;
    justify-content: center;
    gap: 22px;
  }
  .brand-ring {
    width: 96px; height: 96px;
    border: 14px solid var(--accent);
    border-radius: 50%;
  }
  .brand-name {
    font-weight: 700;
    font-size: 54px;
    color: var(--accent);
    line-height: 1;
    white-space: nowrap;
  }
</style>
</head>
<body>

  <section class="card card--front">
    <div class="illustration-area" role="img" aria-label="Faint grey brain illustration in the background"></div>
    <div class="front-wordmark">KEEN FIELD</div>
  </section>

  <section class="card card--back">
    <div class="back-wordmark">KEEN FIELD</div>

    <div class="contact contact--person">
      <svg viewBox="0 0 34 34" aria-hidden="true">
        <circle cx="17" cy="17" r="17" fill="var(--ink)"/>
        <circle cx="17" cy="13" r="5" fill="none" stroke="var(--accent)" stroke-width="2.4"/>
        <path d="M8 27 C9 20 25 20 26 27" fill="none" stroke="var(--accent)" stroke-width="2.4"/>
      </svg>
      <div class="contact-text">Daniel Reed Hart,<br>Director</div>
    </div>

    <div class="brand-lockup">
      <div class="brand-ring"></div>
      <div class="brand-name">KEEN FIELD</div>
    </div>

    <div class="contact contact--email">
      <svg viewBox="0 0 34 34" aria-hidden="true">
        <circle cx="17" cy="17" r="17" fill="var(--ink)"/>
        <rect x="7" y="10" width="20" height="14" fill="none" stroke="var(--accent)" stroke-width="2.2"/>
        <path d="M7 10 L17 18 L27 10 M7 24 L14 16 M27 24 L20 16" fill="none" stroke="var(--accent)" stroke-width="2"/>
      </svg>
      <div class="contact-text">keenfield@mail.com</div>
    </div>
  </section>

</body>
</html>
```